Morvadin Nutrition Supplement Jar

Label for jar. White label on a brown bottle jar.
Conservative look, should look like medicine.
Main Side:
Brightfield Health (smaller size) (with logo)
MORVADIN 10mg (large size)
Doctor Formulated
Developed in Clinical Practice
60 Capsules
(I prefer the single color white label with dark brown letters. Please stay close to that design)
(For the back side, please use the multicolor set up)
(The whole Label should be one color - white with dark brown letters)
Please visit my site for more inspiration and feel: www.calmorvex.com
The product will be brown jar listed on this site.
Can you please provide one version without the text "Brightfield Health & Logo".
Thank you.

Target Market(s)

Women, 34-59 years old

Industry/Entity Type

Nutrition

Requirements
Should not have
• Multicolors, leaves,

```html
<!DOCTYPE html>
<html lang="en">
<head>
<meta charset="utf-8">
<title>Morvadin Label</title>
<link rel="stylesheet" href="https://fonts.googleapis.com/css2?family=Inter:wght@300;400;500;600;700;800&display=swap">
<style>
  :root {
    --page: #ffffff;
    --label: #ffffff;
    --ink: #1c1c1c;
    --ink-soft: #555555;
    --rule: #9a9a9a;
    --frame: #3a3a3a;
    --accent: #c9a24a;
  }
  * { margin: 0; padding: 0; box-sizing: border-box; }
  html, body {
    width: 1200px; height: 2826px; overflow: hidden;
    background: var(--page);
    font-family: "Inter", Arial, sans-serif;
    color: var(--ink);
  }
  .label {
    position: absolute; left: 76px; top: 1226px;
    width: 1048px; height: 374px;
    background: var(--label);
    border: 1px solid var(--frame);
  }
  .label > * { position: absolute; }

  /* back panel */
  .facts-title { left: 29px; top: 24px; font-size: 10px; font-weight: 700; }
  .facts-row { left: 29px; font-size: 8.5px; }
  .facts-row span { display: inline-block; width: 119px; }
  .rule { left: 29px; width: 310px; height: 1px; background: var(--rule); }
  .copy { left: 29px; width: 310px; font-size: 7.2px; line-height: 1.3; color: var(--ink-soft); text-align: justify; }
  .copy strong { color: var(--ink); font-weight: 700; }
  .formula-head { left: 29px; top: 89px; font-size: 8.3px; color: var(--ink); }
  .maker { left: 29px; top: 267px; font-size: 8px; line-height: 1.3; color: var(--ink-soft); }
  .maker strong { color: var(--ink); font-weight: 700; }
  .address { left: 29px; font-size: 8px; line-height: 1.3; color: var(--ink-soft); }
  .fda-box {
    left: 174px; top: 296px; width: 169px; height: 51px;
    border: 1.5px solid var(--ink);
    padding: 4px 6px; font-size: 7.6px; font-weight: 700; line-height: 1.25; text-align: left;
  }

  /* spine */
  .spine-name {
    left: 524px; top: 189px;
    transform: translate(-50%, -50%) rotate(-90deg);
    white-space: nowrap; font-size: 24px; font-weight: 300; letter-spacing: 0.2px;
  }
  .spine-name b { font-weight: 700; }

  /* front panel */
  .brand { left: 742px; top: 38px; display: flex; align-items: center; gap: 8px; }
  .brand-dot { width: 40px; height: 40px; border-radius: 50%; border: 2px solid var(--accent); }
  .brand-name { font-size: 18px; font-weight: 400; }
  .product-name { left: 744px; top: 140px; font-size: 46px; font-weight: 700; letter-spacing: -0.5px; }
  .name-rule { left: 748px; top: 211px; width: 117px; height: 1.5px; background: var(--ink); }
  .strength { left: 888px; top: 196px; font-size: 22px; font-weight: 300; }
  .claim { left: 742px; font-size: 11.5px; }
  .claim-main { top: 272px; font-weight: 500; }
  .claim-sub { top: 288px; color: var(--ink-soft); }
  .count { left: 742px; top: 317px; font-size: 11.5px; padding-bottom: 3px; border-bottom: 1px solid var(--ink); }
</style>
</head>
<body>
  <section class="label">
    <h2 class="facts-title">Supplement Facts</h2>
    <p class="facts-row" style="top:46px"><span>Serving Size:</span>1 capsule</p>
    <p class="facts-row" style="top:60px"><span>Servings per Container:</span>60</p>
    <div class="rule" style="top:79px"></div>
    <p class="formula-head">Proprietary Formula: 1800 mg (% of Daily Value not Established)</p>
    <p class="copy" style="top:102px">Thiamin hydrochloride, Riboflavin, Niacinamide, Pyridoxine hydrochloride, Folic Acid, Cyanocobalamin, Biotin, Pueraria Root, Lithium Orotate, Gentian Root, Bupleurum Root, Milk Thistle Seed Extract, Angelica Root, Chanca Piedra, Dandelion Root, Rhodiola Rosea, Saffron.</p>
    <div class="rule" style="top:152px"></div>
    <p class="copy" style="top:160px"><strong>Directions:</strong> Take one or two capsules after meals. Do not exceed three capsules per day. Take during real-time cravings or before drinking situations for additional craving support. Store in a cool dry place, tightly closed. Keep away from children.</p>
    <p class="copy" style="top:203px"><strong>Warning:</strong> Not to be used by children under 18 years, women who are pregnant, may become pregnant, breastfeeding, people taking antidepressant drugs or sedatives. If you are under a physician's care or taking any medications, or being treated for heart disease or diabetes, consult your health care professional before taking this product.</p>
    <div class="rule" style="top:252px"></div>
    <p class="maker">Manufactured in the USA for<br><strong>Calmorvex LLC</strong><br>from Globally Sourced Ingredients</p>
    <p class="address" style="top:312px">Calmorvex LLC,<br>Aurora, Colorado<br>Ph. 555-014-2290,<br>www.calmorvex.com</p>
    <p class="fda-box">The FDA has not evaluated these statements. This product is not intended to diagnose, treat, cure, or prevent any disease.</p>

    <p class="spine-name"><b>Brightfield</b> Health.</p>

    <div class="brand">
      <span class="brand-dot" aria-hidden="true"></span>
      <span class="brand-name">Brightfield Health</span>
    </div>
    <h1 class="product-name">MORVADIN</h1>
    <div class="name-rule"></div>
    <p class="strength">10mg</p>
    <p class="claim claim-main">Doctor Formulated</p>
    <p class="claim claim-sub">Developed in Clinical Practice</p>
    <p class="count">60 Capsules</p>
  </section>
</body>
</html>
```